Dental Office Looking for Modern, simple business cards

We just acquired our logo. Now we would like to make business cards. We are a dental office with two doctors. We are husband and wife and have a small boutique dental practice in a small town. We love our patients and they are always asking us to give our business cards to their friends. Please help us make business cards :-)

Target Market(s)

30-60 yr old

Industry/Entity Type

Dental Clinic

Contact Information for Business Card

Birch Hollow Dental P.C.
Family and Cosmetic Dentistry
4826 Delmore Rd. Schenectady NY 12417
Tel: 518 642 7731 Fax: 518 642 7048

Dr. Tomas K. Brellin DDS
Dr. Marisol Ede Thornquist DDS

Font styles to use
Serif
Sans Serif

Requirements
Must have
• Simple clean design, modern, colorful. Should incorporate the logo.
Nice to have
• dental imagery ( teeth, smile, etc ...).

```html
<!DOCTYPE html>
<html lang="en">
<head>
<meta charset="utf-8">
<title>Birch Hollow Dental – Business Cards</title>
<link rel="stylesheet" href="https://fonts.googleapis.com/css2?family=Cinzel:wght@500&family=Lora:ital,wght@0,400;0,700;1,600&display=swap">
<style>
  :root {
    --backdrop: #2a2a2c;
    --card: #ffffff;
    --brand-blue: #1577c4;
    --wave-grey: #8a8b8e;
    --ink-white: #ffffff;
    --skin-light: #f3dccd;
    --skin-mid: #e9c4ad;
  }
  html, body {
    margin: 0;
    width: 1200px;
    height: 880px;
    overflow: hidden;
    background: var(--backdrop);
  }
  .sheet {
    width: 1200px;
    height: 880px;
    display: flex;
    flex-direction: column;
    align-items: center;
    justify-content: center;
    gap: 56px;
  }
  .card {
    position: relative;
    width: 640px;
    height: 366px;
    background: var(--card);
    border-radius: 22px;
    overflow: hidden;
    box-shadow: 0 14px 30px rgba(0,0,0,.45);
  }
  .brand-name {
    font-family: "Cinzel", serif;
    font-weight: 500;
    color: var(--brand-blue);
    letter-spacing: 0.04em;
    white-space: nowrap;
    margin: 0;
  }
  .card-front .brand-name {
    position: absolute;
    inset: 0;
    display: flex;
    align-items: center;
    justify-content: center;
    font-size: 42px;
  }
  .card-back .artwork {
    position: absolute;
    inset: 0;
  }
  .card-back .brand-name {
    position: absolute;
    top: 34px;
    right: 34px;
    font-size: 28px;
  }
  .doctors {
    position: absolute;
    top: 90px;
    right: 34px;
    margin: 0;
    text-align: right;
    font-family: "Lora", serif;
    font-style: italic;
    font-weight: 600;
    font-size: 15px;
    line-height: 1.6;
    color: var(--brand-blue);
  }
  .contact {
    position: absolute;
    right: 30px;
    bottom: 26px;
    margin: 0;
    text-align: right;
    font-family: "Lora", serif;
    font-size: 14px;
    line-height: 1.65;
    color: var(--ink-white);
  }
  .contact b { font-weight: 700; }
</style>
</head>
<body>
<main class="sheet">
  <section class="card card-front">
    <p class="brand-name">Birch Hollow Dental</p>
  </section>

  <section class="card card-back">
    <svg class="artwork" width="640" height="366" viewBox="0 0 640 366">
      <defs>
        <linearGradient id="portrait-tone" x1="0" y1="0" x2="1" y2="0">
          <stop offset="0" stop-color="var(--skin-mid)"/>
          <stop offset="0.38" stop-color="var(--skin-light)"/>
          <stop offset="0.62" stop-color="#ffffff"/>
        </linearGradient>
      </defs>
      <rect role="img" aria-label="Photo of a smiling woman touching her cheek" x="0" y="0" width="640" height="366" fill="url(#portrait-tone)"/>
      <path class="wave-grey" d="M0,292 C170,306 290,290 360,230 C420,180 480,156 640,150 L640,366 L0,366 Z" fill="var(--wave-grey)"/>
      <path class="wave-gap" d="M0,306 C170,320 298,302 368,242 C428,192 488,168 640,162 L640,366 L0,366 Z" fill="#ffffff"/>
      <path class="wave-blue" d="M0,316 C170,330 304,312 374,252 C434,202 494,178 640,172 L640,366 L0,366 Z" fill="var(--brand-blue)"/>
    </svg>

    <p class="brand-name">Birch Hollow Dental</p>

    <p class="doctors">
      Dr. Tomas K. Brellin DDS<br>
      Dr. Marisol Ede Thornquist DDS
    </p>

    <p class="contact">
      Family and Cosmetic Dentistry<br>
      4826 Delmore Rd. Schenectady NY 12417<br>
      <b>Tel:</b> 518 642 7731 | <b>Fax:</b> 518 642 7048
    </p>
  </section>
</main>
</body>
</html>
```